Real estate agent : RT Estates

I have done the attached logo designed by your company .
My business card description as below:
Name : Daniel Brooks
Mobile: 0412583047
Email : danielb@rtestates-demo.net.au
Sales & Property Management

```html
<!DOCTYPE html>
<html lang="en">
<head>
<meta charset="utf-8">
<title>RT Estates – Business Card</title>
<link href="https://fonts.googleapis.com/css2?family=Arimo:wght@400;700&family=Montserrat:wght@600&display=swap" rel="stylesheet">
<style>
  :root {
    --backdrop: #e4e4e4;
    --card-light: #ffffff;
    --card-dark: #2f2f2f;
    --ink: #2b2b2b;
    --ink-soft: #3a3a3a;
    --paper-text: #ffffff;
    --rule: #3a3a3a;
  }
  * { margin: 0; padding: 0; box-sizing: border-box; }
  html, body {
    width: 1200px;
    height: 801px;
    overflow: hidden;
    background: var(--backdrop);
  }
  .stage {
    width: 1200px;
    height: 801px;
    display: flex;
    align-items: center;
    justify-content: center;
    gap: 48px;
  }
  .card {
    width: 525px;
    height: 300px;
    position: relative;
    box-shadow: 0 2px 6px rgba(0,0,0,0.12);
  }
  .card--front { background: var(--card-light); color: var(--ink); }
  .card--back {
    background: var(--card-dark);
    color: var(--paper-text);
    display: flex;
    align-items: center;
    justify-content: center;
  }
  .brand {
    font-family: "Montserrat", sans-serif;
    font-weight: 600;
    letter-spacing: 0.04em;
    display: flex;
    align-items: center;
    gap: 10px;
  }
  .brand__dot {
    width: 12px;
    height: 12px;
    border-radius: 50%;
    background: currentColor;
    flex: none;
  }
  .card--front .brand {
    position: absolute;
    left: 52px;
    top: 50%;
    transform: translateY(-50%);
    font-size: 27px;
    color: var(--ink);
  }
  .card--back .brand { font-size: 48px; }
  .divider {
    position: absolute;
    left: 236px;
    top: 104px;
    width: 1px;
    height: 92px;
    background: var(--rule);
  }
  .contact {
    position: absolute;
    left: 258px;
    top: 92px;
    font-family: "Arimo", sans-serif;
    color: var(--ink-soft);
  }
  .contact__name {
    font-weight: 700;
    font-size: 19px;
    letter-spacing: 0.02em;
    text-transform: uppercase;
    color: var(--ink);
  }
  .contact__role { font-size: 14px; margin-top: 2px; }
  .contact__list { list-style: none; margin-top: 20px; font-size: 14.5px; }
  .contact__item { display: flex; align-items: center; gap: 9px; margin-bottom: 5px; }
  .contact__icon { width: 11px; height: 11px; flex: none; }
</style>
</head>
<body>
  <main class="stage">
    <section class="card card--front" aria-label="Business card front">
      <div class="brand"><span class="brand__dot"></span>RT Estates</div>
      <div class="divider"></div>
      <div class="contact">
        <p class="contact__name">Daniel Brooks</p>
        <p class="contact__role">Sales &amp; Property Management</p>
        <ul class="contact__list">
          <li class="contact__item">
            <svg class="contact__icon" viewBox="0 0 24 24" aria-hidden="true"><path fill="currentColor" d="M6.6 10.8a15.1 15.1 0 0 0 6.6 6.6l2.2-2.2a1 1 0 0 1 1-.25 11.4 11.4 0 0 0 3.6.57 1 1 0 0 1 1 1V20a1 1 0 0 1-1 1A17 17 0 0 1 3 4a1 1 0 0 1 1-1h3.5a1 1 0 0 1 1 1c0 1.25.2 2.45.57 3.57a1 1 0 0 1-.25 1z"/></svg>
            <span>0412583047</span>
          </li>
          <li class="contact__item">
            <svg class="contact__icon" viewBox="0 0 24 24" aria-hidden="true"><rect x="2" y="4" width="20" height="16" rx="1.5" fill="none" stroke="currentColor" stroke-width="2.2"/><path d="M3 5.5l9 7 9-7" fill="none" stroke="currentColor" stroke-width="2.2"/></svg>
            <span>danielb@rtestates-demo.net.au</span>
          </li>
        </ul>
      </div>
    </section>
    <section class="card card--back" aria-label="Business card back">
      <div class="brand"><span class="brand__dot"></span>RT Estates</div>
    </section>
  </main>
</body>
</html>
```